Skill Up Salary Up

Full Page
7.5 w x 10 h / 8 w x 10.75 h + .25" bleed
Full-Page Career Course Ad
Project Overview
• Goal: Create a visually attractive, modern, and uncluttered full-page magazine advertisement to list available career courses.
• Tone: Creative, professional, and attention-grabbing to prevent the reader from turning the page. The final design must prioritize readability.

Content Requirements
1. Header/Headline: Must be the primary focus. And grab peoples attention
2. Course Listing: A clear, well-organized list of the career courses.
________________________________________
Design & Aesthetic Directives
1. Layout & Readability (Crucial)
• The final ad must not look crowded or busy.
• Prioritize white space to make the text "breathe" and ensure the course list is easy to scan and read.
• Use a modern, clean, and professional typeface (font choice is critical for the aesthetic).
2. Visual Style
• Aim for a creative, modern, and fresh look. Avoid outdated or generic stock imagery/layouts.
3. Imagery/Graphic Element (Artist's Choice)
You have creative freedom regarding the main graphic element.
• Option A (Photography): Use a photo of a white male American with a collared shirt. The imagery should convey success, focus, or professional development.
• Option B (Vector/Illustration): Use a modern vector graphic, illustration, or abstract design. This could be used to symbolize growth, connection, or a career path.
The choice of graphic element is yours, but it must support the overall modern and uncrowded aesthetic.

Requirements
Must have
• Partial listing .. is part of the Harbor Lantern Course

```html
<!DOCTYPE html>
<html lang="en">
<head>
<meta charset="UTF-8">
<title>Skill Up Salary Up – Upcoming ELM Courses</title>
<link href="https://fonts.googleapis.com/css2?family=Poppins:wght@400;500;600;700;800&display=swap" rel="stylesheet">
<style>
:root{
  --navy:#11304f;
  --gold:#f8b020;
  --ink:#1b1f24;
  --white:#ffffff;
  --rule:#9aa0a6;
  --photo-a:#8d8f93;
  --photo-b:#cfd2d6;
}
*{margin:0;padding:0;box-sizing:border-box}
html,body{width:1004px;height:1200px;overflow:hidden;background:var(--white)}
body{font-family:"Poppins",sans-serif;color:var(--ink)}
.ad{position:relative;width:1004px;height:1200px;background:var(--white);overflow:hidden}
.abs{position:absolute;white-space:nowrap}
.shapes{position:absolute;left:0;top:0}
.tagline{left:67px;top:44px;font-size:38px;font-weight:800;color:var(--navy);letter-spacing:-.5px}
.tagline span{color:var(--gold)}
.hero-upcoming{left:62px;top:118px;font-size:67px;font-weight:400;color:var(--white);letter-spacing:-1px;line-height:1}
.hero-brand{left:58px;top:186px;font-size:190px;font-weight:800;color:var(--gold);line-height:1;letter-spacing:-4px}
.hero-courses{left:62px;top:348px;font-size:84px;font-weight:800;color:var(--white);line-height:1;letter-spacing:-2px}
.pill{position:absolute;top:454px;height:38px;border-radius:10px;display:flex;align-items:center;gap:9px;padding-left:10px;font-size:21px;font-weight:700;border:3px solid var(--white)}
.pill.gold{background:var(--gold);color:var(--navy)}
.pill.navy{background:var(--navy);color:var(--white)}
.tick{width:16px;height:16px;flex:none}
.pill .tick{width:24px;height:24px}
.course-title{font-size:22px;font-weight:700;color:var(--navy);letter-spacing:-.2px}
.course-title span{color:var(--gold)}
.course-sub{font-size:15.5px;font-weight:600;color:var(--ink)}
.ticks{display:flex;gap:12px;font-size:13px;font-weight:400}
.ticks li,.grid li,.box-list li{list-style:none;display:flex;align-items:center;gap:5px;white-space:nowrap}
.ticks .tick,.grid .tick{width:12px;height:12px}
.badge{position:absolute;display:flex;height:27px;font-size:16px;font-weight:700}
.badge b{display:flex;align-items:center;padding:0 8px;background:var(--navy);color:var(--white)}
.badge i{font-style:normal;display:flex;align-items:center;padding:0 10px;background:var(--gold);color:var(--navy)}
.badge.on-gold i{background:var(--white)}
.label{font-size:16px;font-weight:600;color:var(--ink)}
.grid{display:grid;grid-template-columns:104px 102px 146px auto;row-gap:5px;font-size:13px}
.rule{position:absolute;left:67px;width:515px;height:1px;background:var(--rule)}
.box{position:absolute;left:610px;top:527px;width:327px;height:563px;background:var(--gold)}
.box-title{font-size:22px;font-weight:700;color:var(--navy);line-height:1.12}
.box-rank{font-size:17px;font-weight:600;color:var(--navy)}
.box-src{font-size:15px;font-weight:600;color:var(--ink)}
.box-head{font-size:16px;font-weight:700;color:var(--navy)}
.box-list{font-size:13px;line-height:18px;color:var(--ink);display:flex;flex-direction:column;gap:3px}
.box-list .tick,.box-pair .tick{width:12px;height:12px}
.box-pair{display:grid;grid-template-columns:96px auto;row-gap:6px;font-size:13px}
.box-pair li{list-style:none;display:flex;align-items:center;gap:4px}
.box-rule{position:absolute;left:28px;width:276px;height:1px;background:var(--navy);opacity:.5}
.box .abs{left:28px}
</style>
</head>
<body>
<svg width="0" height="0" style="position:absolute">
  <symbol id="tick" viewBox="0 0 24 24">
    <path d="M20 12a8 8 0 1 1-4-6.9" fill="none" stroke="currentColor" stroke-width="2.4" stroke-linecap="round"/>
    <path d="M8 11.5l3.5 3.5L21 5" fill="none" stroke="currentColor" stroke-width="2.6" stroke-linecap="round" stroke-linejoin="round"/>
  </symbol>
</svg>

<main class="ad">
  <svg class="shapes" width="1004" height="500" viewBox="0 0 1004 500">
    <polygon points="0,113 451,113 566,240 497,450 0,463" fill="var(--navy)"/>
    <polygon points="478,150 514,155 568,236 558,266" fill="var(--gold)"/>
    <defs>
      <linearGradient id="photoTone" x1="0" y1="0" x2="1" y2="1">
        <stop offset="0" stop-color="var(--photo-a)"/>
        <stop offset="1" stop-color="var(--photo-b)"/>
      </linearGradient>
    </defs>
    <polygon role="img" aria-label="Photo: a professional man in a white collared shirt holding a notebook, offering a handshake on office steps" points="610,129 974,129 859,450 497,450" fill="url(#photoTone)"/>
  </svg>

  <div class="abs tagline">SKILL UP <span>$ALARY UP</span></div>
  <div class="abs hero-upcoming">UPCOMING</div>
  <div class="abs hero-brand">ELM</div>
  <div class="abs hero-courses">COURSES</div>

  <div class="pill gold" style="left:65px;width:227px"><svg class="tick" style="color:var(--navy)"><use href="#tick"/></svg>MEN &amp; WOMEN</div>
  <div class="pill navy" style="left:296px;width:301px"><svg class="tick" style="color:var(--gold)"><use href="#tick"/></svg>IN-PERSON &amp; REMOTE</div>
  <div class="pill gold" style="left:602px;width:337px"><svg class="tick" style="color:var(--navy)"><use href="#tick"/></svg>PARTIAL SCHOLORASHIPS</div>

  <!-- Harbor Lantern Course -->
  <div class="abs course-title" style="left:67px;top:518px">HARBOR <span>LANTERN</span></div>
  <div class="abs course-sub" style="left:67px;top:551px">Business Skills &amp; Knowledge to</div>
  <ul class="abs ticks" style="left:67px;top:578px">
    <li><svg class="tick" style="color:var(--gold)"><use href="#tick"/></svg>Impress your interviewer</li>
    <li><svg class="tick" style="color:var(--gold)"><use href="#tick"/></svg>Start / Run Your Business</li>
    <li><svg class="tick" style="color:var(--gold)"><use href="#tick"/></svg>Maximize Income</li>
  </ul>
  <div class="badge" style="left:67px;top:610px"><b>4-5 MONTHS</b><i>NOV 2025</i></div>
  <div class="abs label" style="left:67px;top:646px">PARTIAL LISTING</div>
  <ul class="abs grid" style="left:67px;top:677px">
    <li><svg class="tick" style="color:var(--gold)"><use href="#tick"/></svg>Computers</li>
    <li><svg class="tick" style="color:var(--gold)"><use href="#tick"/></svg>Sales</li>
    <li><svg class="tick" style="color:var(--gold)"><use href="#tick"/></svg>LedgerLite</li>
    <li><svg class="tick" style="color:var(--gold)"><use href="#tick"/></svg>Investments</li>
    <li><svg class="tick" style="color:var(--gold)"><use href="#tick"/></svg>Marketing</li>
    <li><svg class="tick" style="color:var(--gold)"><use href="#tick"/></svg>Finance</li>
    <li><svg class="tick" style="color:var(--gold)"><use href="#tick"/></svg>Business Strategy</li>
    <li><svg class="tick" style="color:var(--gold)"><use href="#tick"/></svg>Real Estate</li>
    <li><svg class="tick" style="color:var(--gold)"><use href="#tick"/></svg>Accounting</li>
    <li><svg class="tick" style="color:var(--gold)"><use href="#tick"/></svg>Healthcare</li>
    <li><svg class="tick" style="color:var(--gold)"><use href="#tick"/></svg>Communication</li>
  </ul>
  <div class="rule" style="top:754px"></div>

  <!-- Bookkeeping -->
  <div class="abs course-title" style="left:66px;top:770px">BOOKKEEPING <span>LEDGERLITE</span></div>
  <div class="abs course-sub" style="left:66px;top:803px">Train for a quality job Manage your own books</div>
  <ul class="abs grid" style="left:67px;top:830px;grid-template-columns:213px auto;row-gap:7px">
    <li><svg class="tick" style="color:var(--gold)"><use href="#tick"/></svg>Finance Management</li>
    <li><svg class="tick" style="color:var(--gold)"><use href="#tick"/></svg>Advanced Tools</li>
    <li><svg class="tick" style="color:var(--gold)"><use href="#tick"/></svg>Customer &amp; Vendor Mgmt</li>
    <li><svg class="tick" style="color:var(--gold)"><use href="#tick"/></svg>Customer &amp; Vendor Mgmt</li>
  </ul>
  <div class="badge" style="left:69px;top:887px"><b>5 WEEKS</b><i>NOV 2025</i></div>
  <div class="rule" style="top:935px"></div>

  <!-- Office suite -->
  <div class="abs course-title" style="left:67px;top:950px">OFFICE SUITE <span>COMPUTERS</span></div>
  <div class="abs course-sub" style="left:67px;top:981px">The New Job Prerequisite</div>
  <ul class="abs ticks" style="left:67px;top:1009px">
    <li><svg class="tick" style="color:var(--gold)"><use href="#tick"/></svg>GridCalc</li>
    <li><svg class="tick" style="color:var(--gold)"><use href="#tick"/></svg>MailDesk</li>
    <li><svg class="tick" style="color:var(--gold)"><use href="#tick"/></svg>DocWrite</li>
    <li><svg class="tick" style="color:var(--gold)"><use href="#tick"/></svg>SlideCraft</li>
  </ul>
  <div class="abs course-sub" style="left:67px;top:1031px;font-size:14.5px">Computer lab available to practice</div>
  <div class="badge" style="left:70px;top:1062px"><b>5 WEEKS</b><i>DEC 2025</i></div>

  <!-- Right feature box -->
  <aside class="box">
    <div class="abs box-title" style="top:22px">SOFTWARE, WEB &amp; APPS</div>
    <div class="abs box-rank" style="top:51px">#2 BEST TECH JOB</div>
    <div class="abs box-src" style="top:74px">Civic Career Review 2025</div>
    <div class="abs box-head" style="top:97px">Job Opportunities</div>
    <ul class="abs box-list" style="top:124px">
      <li><svg class="tick" style="color:var(--navy)"><use href="#tick"/></svg>Computer Programmer</li>
      <li><svg class="tick" style="color:var(--navy)"><use href="#tick"/></svg>Software Developer/Mobile</li>
      <li><svg class="tick" style="color:var(--navy)"><use href="#tick"/></svg>Engineer Developer (Apps)</li>
    </ul>
    <div class="abs box-head" style="top:187px;font-size:17px">Optional</div>
    <ul class="abs box-list" style="top:213px">
      <li><svg class="tick" style="color:var(--navy)"><use href="#tick"/></svg>Bachelors in Prog. &amp; Tech</li>
    </ul>
    <div class="badge on-gold" style="left:28px;top:240px"><b>NOV</b><i>2025</i></div>
    <div class="box-rule" style="top:295px"></div>
    <div class="abs box-title" style="top:318px">IT DESKTOP &amp;<br>NETWORKING SUPPORT</div>
    <div class="abs box-rank" style="top:376px">#2 BEST JOB</div>
    <div class="abs box-src" style="top:401px">Civic Career Review 2025</div>
    <div class="abs box-head" style="top:427px">Masters IT</div>
    <ul class="abs box-pair" style="top:455px">
      <li><svg class="tick" style="color:var(--navy)"><use href="#tick"/></svg>Desktop OS</li>
      <li><svg class="tick" style="color:var(--navy)"><use href="#tick"/></svg>Servers</li>
      <li><svg class="tick" style="color:var(--navy)"><use href="#tick"/></svg>Networks</li>
      <li><svg class="tick" style="color:var(--navy)"><use href="#tick"/></svg>Cloud</li>
    </ul>
    <div class="badge on-gold" style="left:28px;top:503px"><b>7 MONTHS</b><i>DEC 2025</i></div>
  </aside>
</main>
</body>
</html>
```